Flyers

Modify Existing Flyer and create another for exterior company
Updates

Previous Brief has been updated- we want to update this existing one also

Target Market(s)

Exterior Remodeling Customers

Industry/Entity Type

Remodeling/Construction

```html
<!DOCTYPE html>
<html lang="en">
<head>
<meta charset="utf-8">
<title>Remodeling Company Flyer</title>
<link rel="stylesheet" href="https://fonts.googleapis.com/css2?family=Montserrat:wght@400;500;600;700;800&display=swap">
<style>
  :root {
    --stage: #2e2f31;
    --paper: #ebe8e3;
    --blue: #1f73c4;
    --orange: #e0531f;
    --peach: #ffd2bd;
    --ink: #1c1c1e;
    --white: #ffffff;
    --navy: #2a4f86;
  }
  * { box-sizing: border-box; margin: 0; padding: 0; }
  html, body { width: 1200px; height: 800px; overflow: hidden; }
  body {
    background: var(--stage);
    font-family: "Montserrat", sans-serif;
    position: relative;
  }
  .flyer {
    position: absolute;
    left: 305px; top: 18px;
    width: 590px; height: 764px;
    background: var(--paper);
    overflow: hidden;
  }
  .flyer-shapes { position: absolute; inset: 0; }

  .brand {
    position: absolute; left: 32px; top: 50px;
    display: flex; align-items: center; gap: 10px;
  }
  .brand-mark { width: 16px; height: 16px; background: var(--orange); flex: none; }
  .brand-name {
    color: var(--navy); font-weight: 700; font-size: 16px;
    line-height: 1.2; text-transform: uppercase; letter-spacing: .5px;
  }

  .hero { position: absolute; left: 30px; top: 178px; color: var(--white); }
  .hero-lead { font-size: 16px; font-weight: 700; line-height: 1.08; }
  .hero-title { font-size: 38px; font-weight: 800; line-height: 1.04; margin-top: 6px; letter-spacing: 1px; }
  .hero-place { font-size: 16px; font-weight: 600; margin-top: 4px; line-height: 1.2; }

  .column-left {
    position: absolute; left: 30px; top: 360px; width: 280px; height: 380px;
    display: flex; flex-direction: column; justify-content: space-between;
  }
  .service { position: absolute; }
  .column-left .service { position: static; }
  .tag {
    display: inline-block; font-size: 12px; font-weight: 800; line-height: 1.2;
    padding: 3px 22px 3px 10px; text-transform: uppercase;
    clip-path: polygon(0 0, 100% 0, calc(100% - 12px) 100%, 0 100%);
  }
  .tag-light { background: var(--white); color: var(--ink); }
  .tag-dark { background: var(--ink); color: var(--white); }
  .intro { font-size: 8px; font-weight: 600; line-height: 1.32; margin-top: 4px; }
  .list { list-style: none; font-size: 8px; line-height: 1.3; margin-top: 3px; }
  .on-orange .intro { color: var(--ink); }
  .on-orange .list { color: var(--peach); }
  .on-paper .intro, .on-paper .list { color: var(--ink); }
  .bullets li::before { content: "• "; }
  .white-stripe {
    height: 10px; width: 270px; background: var(--white);
    clip-path: polygon(0 0, 100% 0, calc(100% - 10px) 100%, 0 100%);
  }

  .additions { left: 334px; top: 440px; width: 240px; }
  .bath-right { left: 334px; top: 584px; width: 246px; }

  .photo { position: absolute; }
  .photo-living {
    left: 334px; top: 330px; width: 112px; height: 100px;
    border: 4px solid var(--blue);
    background: linear-gradient(160deg, #c9ccd2 0%, #e7e1d6 55%, #9a7a5c 100%);
  }
  .photo-lounge {
    left: 470px; top: 500px; width: 110px; height: 74px;
    background: linear-gradient(180deg, #5b6e8a 0%, #8f97a3 55%, #d8d2c8 100%);
  }

  .call {
    position: absolute; left: 340px; top: 694px; width: 250px; height: 44px;
    background: var(--orange); color: var(--white);
    clip-path: polygon(16px 0, 100% 0, 100% 100%, 16px 100%, 0 50%);
    display: flex; align-items: center; gap: 10px; padding-left: 30px;
  }
  .call-icon { width: 18px; height: 18px; flex: none; }
  .call-text { text-align: right; flex: 1; padding-right: 12px; }
  .call-label { font-size: 6.5px; font-weight: 700; letter-spacing: .4px; }
  .call-phone { font-size: 17px; font-weight: 800; line-height: 1.1; }
  .call-web { font-size: 6.5px; font-weight: 700; }
</style>
</head>
<body>
  <main class="flyer">
    <svg class="flyer-shapes" viewBox="0 0 590 764" width="590" height="764">
      <defs>
        <linearGradient id="kitchen-tones" x1="0" y1="0" x2="1" y2="1">
          <stop offset="0" stop-color="#6b6f73"/>
          <stop offset="0.45" stop-color="#3d4347"/>
          <stop offset="0.75" stop-color="#5a4a44"/>
          <stop offset="1" stop-color="#2c3034"/>
        </linearGradient>
      </defs>
      <polygon role="img" aria-label="Photo of a modern kitchen sink with a tall faucet and potted plants"
               points="270,0 590,0 590,434 424,434 250,240" fill="url(#kitchen-tones)"/>
      <polygon class="hero-band" points="0,168 255,168 345,346 0,346" fill="var(--blue)"/>
      <rect class="orange-panel" x="18" y="350" width="302" height="396" fill="var(--orange)"/>
      <rect class="base-band" x="18" y="746" width="302" height="10" fill="var(--blue)"/>
      <rect class="base-band-right" x="320" y="740" width="270" height="6" fill="var(--orange)"/>
    </svg>

    <div class="brand">
      <span class="brand-mark"></span>
      <span class="brand-name">Ridgeline Roofing<br>and Exteriors</span>
    </div>

    <header class="hero">
      <p class="hero-lead">Work with a<br>Top-rated<br>Local</p>
      <h1 class="hero-title">REMODELING<br>COMPANY</h1>
      <p class="hero-place">in Ankeny, IA</p>
    </header>

    <div class="photo photo-living" role="img" aria-label="Photo of a bright living room with a white sofa"></div>
    <div class="photo photo-lounge" role="img" aria-label="Photo of a lounge with a grey sofa and blue wall"></div>

    <div class="column-left">
      <section class="service kitchen on-orange">
        <h2 class="tag tag-light">Kitchen Remodeling</h2>
        <p class="intro">Whatever your vision is for your new kitchen, our crew can help you bring it to life. You can trust us for:</p>
        <ul class="list">
          <li>Open concept design services</li>
          <li>Kitchen cabinet installation services</li>
          <li>Kitchen countertop installation services</li>
          <li>Lighting installation services</li>
          <li>Tile installation services</li>
          <li>Plumbing upgrade services</li>
          <li>Electrical upgrade services</li>
          <li>Drywall services</li>
          <li>Painting services</li>
        </ul>
      </section>

      <section class="service bath-left on-orange">
        <h2 class="tag tag-light">Bathroom Remodeling</h2>
        <p class="intro">When you hire us for your bathroom remodeling project, the possibilities are endless. Our experienced and talented team can:</p>
        <ul class="list bullets">
          <li>Install a custom tile shower</li>
          <li>Build a new vanity</li>
          <li>Install flooring and tile</li>
          <li>Replace your plumbing and light fixtures</li>
        </ul>
      </section>

      <div class="white-stripe"></div>

      <section class="service decks on-orange">
        <h2 class="tag tag-light">Decks/Patios</h2>
        <p class="intro">An outdoor space is a great addition to any residential property. When you decide to build a patio or deck, you'll be able to experience a variety of benefits. Your outdoor area will increase your:</p>
        <ul class="list">
          <li>Property value</li>
          <li>Curb appeal</li>
          <li>Functional living space</li>
        </ul>
      </section>
    </div>

    <section class="service additions on-paper">
      <h2 class="tag tag-dark">Home Additions</h2>
      <p class="intro">No matter what kind of space you need, our team will bring your vision to life. You can hire us if you need a:</p>
      <ul class="list bullets">
        <li>Bathroom addition</li>
        <li>Bedroom addition</li>
        <li>Garage addition</li>
        <li>Basement addition</li>
        <li>Guest room addition</li>
        <li>Living room addition</li>
        <li>Sunroom addition</li>
      </ul>
    </section>

    <section class="service bath-right on-paper">
      <h2 class="tag tag-dark">Bathroom Remodeling</h2>
      <p class="intro">When you hire us for your bathroom remodeling project, the possibilities are endless. Our experienced and talented team can:</p>
      <ul class="list bullets">
        <li>Install a custom tile shower</li>
        <li>Build a new vanity</li>
        <li>Install flooring and tile</li>
        <li>Replace your plumbing and light fixtures</li>
      </ul>
    </section>

    <aside class="call">
      <svg class="call-icon" viewBox="0 0 24 24" aria-hidden="true">
        <path fill="#fff" d="M6.6 10.8a15.1 15.1 0 0 0 6.6 6.6l2.2-2.2a1 1 0 0 1 1-.25 11.4 11.4 0 0 0 3.6.57 1 1 0 0 1 1 1V20a1 1 0 0 1-1 1A17 17 0 0 1 3 4a1 1 0 0 1 1-1h3.5a1 1 0 0 1 1 1c0 1.25.2 2.45.57 3.57a1 1 0 0 1-.25 1z"/>
      </svg>
      <div class="call-text">
        <p class="call-label">CALL TODAY FOR YOUR FREE ESTIMATE</p>
        <p class="call-phone">555-014-2290</p>
        <p class="call-web">WWW.RIDGELINEEXTERIORS.COM</p>
      </div>
    </aside>
  </main>
</body>
</html>
```